Employee Wellbeing Model Graphic Design

A visual/graphic representation of our Employee Wellbeing model.
Our model is a combination of the Ngā Kiri Rehu Pona model of health and wellbeing and the wellbeing continuum.
We would like the visual to be on one page. The design should be modern and simple.
The powerpoint attached shows the information we are wanting to share with our employees about our wellbeing programme.

Target Market(s)

Our employees

Industry/Entity Type

Event Management

Font styles to use
Sans Serif
Other font styles liked:
• calibri light

Colors
00AB8E
00BBA5
67D7C9
C6EFE9
E9F9F6

```html
<!DOCTYPE html>
<html lang="en">
<head>
<meta charset="utf-8">
<title>Our Wellbeing Framework</title>
<link href="https://fonts.googleapis.com/css2?family=Open+Sans:ital,wght@0,400;0,600;0,700;1,400&display=swap" rel="stylesheet">
<style>
:root{
  --teal:#0DB8A5;
  --teal-dark:#00AB8E;
  --teal-mid:#67D7C9;
  --teal-pale:#C6EFE9;
  --teal-wash:#E9F9F6;
  --ink:#1d1d1d;
  --heading-grey:#555555;
  --unwell:#E8245F;
  --struggling:#F5A043;
  --going-ok:#D6C21E;
  --thriving:#5BB56A;
  --spectrum:linear-gradient(90deg,#EC1F6A 0%,#F3875A 25%,#F6A443 42%,#E5BE2B 62%,#D2D12B 75%,#5BBB6A 100%);
}
*{box-sizing:border-box;margin:0;padding:0}
html,body{width:893px;height:1200px;overflow:hidden;background:#fff}
body{font-family:"Open Sans",Calibri,Arial,sans-serif;color:var(--ink);position:relative}
.sheet{position:absolute;inset:0}

.header-band{position:absolute;left:0;top:0;width:640px;height:84px}
.header-title{position:absolute;left:62px;top:23px;font-size:30px;font-weight:700;color:#fff;letter-spacing:.3px}
.brand{position:absolute;left:660px;top:16px;width:190px;text-align:center;color:var(--teal-dark);font-weight:700;font-size:26px;letter-spacing:4px;line-height:30px}

.whare-art{position:absolute;left:28px;top:113px;width:263px;height:168px;border-radius:4px;background:linear-gradient(160deg,var(--teal-mid),var(--teal))}

.model-heading{position:absolute;left:309px;top:100px;font-size:20px;font-weight:700;color:var(--heading-grey)}
.model-intro{position:absolute;left:309px;top:132px;width:515px;font-size:13px;line-height:18px}
.pillar{position:absolute;width:167px}
.pillar-name{height:19px;background:var(--teal);color:#fff;border-radius:4px;font-size:11px;font-weight:700;line-height:19px;padding-left:9px}
.pillar-desc{font-size:11px;font-style:italic;color:#333;margin-top:4px;padding-left:4px}
.pillar-desc::before{content:"• ";font-style:normal}

.stage{position:absolute;top:305px;font-size:11px;font-weight:700;transform:translateX(-50%)}
.stage.unwell{left:196px;color:var(--unwell)}
.stage.struggling{left:388px;color:var(--struggling)}
.stage.going-ok{left:583px;color:var(--going-ok)}
.stage.thriving{left:776px;color:var(--thriving)}

.spectrum-bar{position:absolute;left:109px;width:751px;height:14px;border-radius:7px;background:var(--spectrum)}

.side-tab{position:absolute;left:0;width:82px;background:var(--teal);color:#fff;display:flex;align-items:center;justify-content:center}
.side-tab .tab-text{writing-mode:vertical-rl;transform:rotate(180deg);text-align:center}
.tab-title{font-size:15px;font-weight:700;line-height:20px;white-space:nowrap}
.tab-sub{font-size:14px;font-style:italic;line-height:20px;white-space:nowrap}
.tab-continuum{top:331px;height:251px;border-radius:0 0 18px 0}
.tab-signs{top:595px;height:281px;border-radius:0 18px 18px 0}
.tab-initiatives{top:891px;height:309px;border-radius:0 18px 0 0}

.section-note{position:absolute;left:112px;width:752px;font-size:11.2px;font-style:italic;line-height:15.5px}

.col{position:absolute;list-style:none;font-size:11.2px;line-height:15.5px}
.col li{position:relative;padding-left:12px}
.col li::before{content:"";position:absolute;left:2px;top:6px;width:4px;height:4px;border-radius:50%;background:var(--ink)}

.approach{position:absolute;top:952px}
.approach-name{font-size:11.2px;font-weight:700;color:var(--teal)}
.approach-desc{font-size:11.2px}
.programme-heading{position:absolute;left:0;width:893px;padding-left:100px;top:990px;text-align:center;font-size:15.5px;font-weight:700;color:var(--teal)}

.whare-faint{position:absolute;left:84px;top:1040px;width:316px;height:160px;background:var(--teal-wash);opacity:.6}
</style>
</head>
<body>
<main class="sheet">

  <svg class="header-band" viewBox="0 0 640 84" aria-hidden="true">
    <polygon points="0,0 633,0 597,84 0,84" fill="var(--teal)"/>
  </svg>
  <h1 class="header-title">OUR WELLBEING FRAMEWORK</h1>
  <div class="brand">KAHU<br>EVENTS</div>

  <div class="whare-art" role="img" aria-label="Illustration of a whare with a central pou, labelled Ngā Kiri Rehu Pona"></div>

  <h2 class="model-heading">NGĀ KIRI REHU PONA</h2>
  <p class="model-intro">When all these things are in balance, we thrive. When one or more of these is out of balance our wellbeing is impacted. By aligning workplace activities with Ngā Kiri Rehu Pona, organizations can create an environment where well-being is valued, and employees thrive</p>

  <div class="pillar" style="left:311px;top:214px"><div class="pillar-name">TAHA HINENGARO</div><div class="pillar-desc">Mental/Emotional Heath</div></div>
  <div class="pillar" style="left:491px;top:214px"><div class="pillar-name">TAHA WHANAU</div><div class="pillar-desc">Family/Community Health</div></div>
  <div class="pillar" style="left:673px;top:214px"><div class="pillar-name">WHENUA</div><div class="pillar-desc">Land/Roots</div></div>
  <div class="pillar" style="left:311px;top:258px"><div class="pillar-name">TAHA TINANA</div><div class="pillar-desc">Physical Health</div></div>
  <div class="pillar" style="left:491px;top:258px"><div class="pillar-name">TAHA WAIRUA</div><div class="pillar-desc">Spiritual Health</div></div>

  <div class="stage unwell">UNWELL</div>
  <div class="stage struggling">STRUGGLING</div>
  <div class="stage going-ok">GOING OK</div>
  <div class="stage thriving">THRIVING</div>

  <div class="spectrum-bar" style="top:331px"></div>
  <div class="side-tab tab-continuum"><div class="tab-text"><div class="tab-title">The Wellbeing Continuum</div></div></div>
  <p class="section-note" style="top:350px">People can have a range of mental health experiences across the continuum that will change over time. It is usual to cycle across the Thriving and Going Ok parts of the spectrum.</p>

  <ul class="col" style="left:112px;top:385px;width:170px">
    <li>People who are mentally unwell and/or have a diagnosed mental illness</li>
    <li>Severe and persistent functional impairment</li>
    <li>Neurochemical process outside of the individuals’ control is often established</li>
  </ul>
  <ul class="col" style="left:299px;top:385px;width:185px">
    <li>People who don’t meet the criteria for a diagnosable mental illness, but who may be highly stressed or distressed</li>
    <li>More severe and persistent functional impairment</li>
    <li>A mental health problem develops</li>
    <li>Usual coping mechanisms may not suffice or don’t have the same impact</li>
  </ul>
  <ul class="col" style="left:490px;top:385px;width:210px">
    <li>People who lack general mental wellbeing and a sense of being reasonably happy with life</li>
    <li>Often show as disengaged and unmotivated, lack meaning and purpose in their daily lives</li>
    <li>Likely to have higher rates of physical illness and workplace accidents</li>
    <li>People develop coping mechanisms which can be applied to help revert to full mental health – thriving</li>
  </ul>
  <ul class="col" style="left:700px;top:385px;width:165px">
    <li>People who are mentally unwell and/or have a diagnosed mental illness</li>
    <li>Severe and persistent functional impairment</li>
    <li>Neurochemical process outside of the individuals’ control is often established</li>
  </ul>

  <div class="spectrum-bar" style="top:582px"></div>
  <div class="side-tab tab-signs"><div class="tab-text"><div class="tab-title">The Wellbeing Continuum</div><div class="tab-sub">Signs and Symptoms</div></div></div>
  <p class="section-note" style="top:601px">People can have a range of mental health experiences across the continuum that will change over time. It is usual to cycle across the Thriving and Going Ok parts of the spectrum</p>

  <ul class="col" style="left:112px;top:636px;width:180px">
    <li>Angry outbursts/aggression</li>
    <li>Excessive anxiety/panic attacks</li>
    <li>Thoughts of suicide</li>
    <li>Can’t perform duties, control behaviour or concentrate</li>
    <li>Can’t fall asleep or stay asleep</li>
    <li>Sleeping too much or too little</li>
    <li>Physical illness</li>
    <li>Constant fatigue</li>
    <li>Not going out/answering phone</li>
    <li>Substance or gambling addiction</li>
    <li>Other addictions</li>
  </ul>
  <ul class="col" style="left:299px;top:636px;width:190px">
    <li>Anger</li>
    <li>Anxiety</li>
    <li>Pervasively sad/hopeless</li>
    <li>Negative attitude</li>
    <li>Poor performance/workaholic</li>
    <li>Poor concentration/decisions</li>
    <li>Restless disturbed sleep</li>
    <li>Recurrent images/nightmares</li>
    <li>Increased aches and pains</li>
    <li>Increased fatigue</li>
    <li>Avoidance</li>
    <li>Withdrawal</li>
    <li>Increased substance use/gambling hard to control</li>
  </ul>
  <ul class="col" style="left:490px;top:636px;width:210px">
    <li>Irritable/impatient</li>
    <li>Nervous</li>
    <li>Sadness/overwhelmed</li>
    <li>Procrastination</li>
    <li>Forgetfulness</li>
    <li>Trouble sleeping</li>
    <li>Intrusive thoughts</li>
    <li>Nightmares</li>
    <li>Muscle tension/headaches</li>
    <li>Low energy</li>
    <li>Decreased activity/ socialising</li>
    <li>Regular but controlled substance use or gambling</li>
  </ul>
  <ul class="col" style="left:700px;top:636px;width:170px">
    <li>Normal mood fluctuations</li>
    <li>Calm and takes things in stride</li>
    <li>Good sense of humour</li>
    <li>Performing well</li>
    <li>In control mentally</li>
    <li>Normal sleep patterns</li>
    <li>Few sleep difficulties</li>
    <li>Physically well</li>
    <li>Good energy levels</li>
    <li>Physically and socially active</li>
    <li>Not using substances to cope</li>
    <li>None or limited gambling</li>
  </ul>

  <div class="spectrum-bar" style="top:877px"></div>
  <div class="side-tab tab-initiatives"><div class="tab-text"><div class="tab-title">Applying the Wellbeing Continuum</div><div class="tab-sub">Our Wellbeing Initiatives</div></div></div>
  <p class="section-note" style="top:897px">Our approach is to provide a programme of wellbeing interventions across the continuum, and ensure our initiatives align with the Ngā Kiri Rehu Pona model by providing support for physical health, mental/emotional health, family and community health, spiritual health and connection to whenua.</p>

  <div class="whare-faint" role="img" aria-label="Faint whare illustration in the background"></div>

  <div class="approach" style="left:112px"><div class="approach-name">Treatment</div><div class="approach-desc">Providing Help, Supporting Recovery</div></div>
  <div class="approach" style="left:354px"><div class="approach-name">Building Capability</div><div class="approach-desc">Changing Mindsets, Raising Awareness</div></div>
  <div class="approach" style="left:621px"><div class="approach-name">Prevention</div><div class="approach-desc">Reducing Risks, Staying Well</div></div>

  <h3 class="programme-heading">OUR PROGRAMME OF WELLBEING INITIATIVES</h3>

  <ul class="col" style="left:112px;top:1018px;width:235px">
    <li>Occupational Counselling (OCP)</li>
    <li>Domestic Violence Leave</li>
    <li>Injury Management (Kinetic Care)</li>
    <li>Psychological First Aiders</li>
  </ul>
  <ul class="col" style="left:376px;top:1018px;width:245px">
    <li>Wellbeing Intranet Site</li>
    <li>Wellbeing Training Module in LearnLoop</li>
    <li>Lend a Hand (volunteer) Day</li>
    <li>Positive Leadership Programme</li>
    <li>Regular Staff Engagement Activities</li>
    <li>Wellbeing Campaigns</li>
    <li>Culture Committee</li>
    <li>ClearPath e-learning for Managers</li>
  </ul>
  <ul class="col" style="left:621px;top:1018px;width:250px">
    <li>Wellness Days</li>
    <li>Annual Health Monitoring</li>
    <li>Flu Vaccinations</li>
    <li>Bullying &amp; Harassment Prevention Policy</li>
    <li>Flexible Work Options</li>
    <li>Fatigue Management Guidelines</li>
    <li>Recreation Leave Purchase</li>
    <li>Health and Wellbeing Policy</li>
    <li>Sick leave available from day 1 of employment</li>
    <li>RideWork for Business</li>
  </ul>

</main>
</body>
</html>
```